Dovrin MC celebrates 16 years

Dovrin Marketing Communication was established in 2000 by Mira Kestelman and is known as one of the leading companies in Israel for Public Relations and marketing communications, with rich experience in every technology sector. Most of our client activities are based on our areas of expertise covering a wide range of Tech, High-tech, Internet and consumer devices.
We need an email signature and a banner that we will promote in our emails body and by social media. The main mesages:
16 years of success, working with global tech companies in Israel, PR and Social Media, strategic and crisis management.
See more setails: www.dovrin-mc.example.co.il

Target Market(s)

we are looking for hitech global companies that want to be promoted in Israel - by PR, Social media and more marketing communication services

Industry/Entity Type

Tech

Font styles to use
Sans Serif
Decorative

Requirements
Must have
• 1.Business and series company but colorful, creative and enthusiasm
• 2. Connection to Dovrin's logo (green) but with more colorful - not too childish
• 3. messages of global, tech and marketing communications
Nice to have
• I have no idea..
Should not have
• not too childish. we are a series company
• please don't design as tech companies - boring...

```html
<!DOCTYPE html>
<html lang="en">
<head>
<meta charset="utf-8">
<title>Dovrin MC – 16 Years Banner</title>
<link rel="stylesheet" href="https://fonts.googleapis.com/css2?family=Montserrat:wght@700&family=Varela+Round&family=Oswald:wght@500&display=swap">
<style>
  :root {
    --page-bg: #e6e6e6;
    --ink: #1c1c1c;
    --brand-green: #8cc63f;
    --panel-green: #b3d25a;
    --band-dark: #222222;
    --muted: #6b6b6b;
    --button-border: #2a2a2a;
  }
  * { margin: 0; padding: 0; box-sizing: border-box; }
  html, body {
    width: 1200px; height: 1200px; overflow: hidden;
    background: var(--page-bg);
  }
  .stage {
    position: relative; width: 1200px; height: 1200px;
  }
  .banner {
    position: absolute;
    left: 94px; top: 490px;
    width: 1180px; height: 272px;
    transform: scale(0.857);
    transform-origin: 0 0;
    overflow: hidden;
    box-shadow: 0 2px 6px rgba(0,0,0,0.35);
    background: #ffffff;
  }
  .banner-shapes { position: absolute; inset: 0; }
  .brand {
    position: absolute; left: 465px; top: 28px;
    display: flex; align-items: center; gap: 12px;
  }
  .brand-square {
    width: 64px; height: 78px; border-radius: 8px;
    background: var(--brand-green);
  }
  .brand-name {
    font-family: "Montserrat", sans-serif; font-weight: 700;
    font-size: 28px; color: var(--brand-green); line-height: 1;
    margin-top: 22px;
  }
  .brand-sub {
    position: absolute; left: 541px; top: 98px;
    font-family: "Varela Round", sans-serif; font-size: 10px;
    color: var(--muted); white-space: nowrap;
  }
  .headline {
    position: absolute; left: 380px; top: 128px; width: 410px;
    text-align: center;
    font-family: "Montserrat", sans-serif; font-weight: 700;
    font-size: 58px; line-height: 54px; letter-spacing: 0.5px;
  }
  .headline .years { color: var(--ink); display: block; }
  .headline .success { color: var(--brand-green); display: block; }
  .services {
    position: absolute; right: 58px; top: 46px;
    text-align: right;
    font-family: "Varela Round", sans-serif; font-size: 19px;
    line-height: 26px; color: var(--ink); letter-spacing: -0.3px;
  }
  .cta {
    position: absolute; left: 893px; top: 175px;
    width: 230px; height: 58px; border-radius: 29px;
    border: 3px solid var(--button-border);
    background: linear-gradient(#ffffff, #e4e4e4);
    display: flex; align-items: center; justify-content: center;
    font-family: "Oswald", sans-serif; font-weight: 500;
    font-size: 24px; color: var(--ink); letter-spacing: 0.2px;
    box-shadow: 0 3px 5px rgba(0,0,0,0.25);
  }
</style>
</head>
<body>
<div class="stage">
  <section class="banner">
    <svg class="banner-shapes" viewBox="0 0 1180 272" width="1180" height="272">
      <defs>
        <radialGradient id="centerGlow" cx="0.5" cy="0.4" r="0.6">
          <stop offset="0" stop-color="#ffffff"/>
          <stop offset="1" stop-color="#ececec"/>
        </radialGradient>
        <linearGradient id="crowdTone" x1="0" y1="0" x2="0" y2="1">
          <stop offset="0" stop-color="#e3e7ef"/>
          <stop offset="0.45" stop-color="#5a6690"/>
          <stop offset="1" stop-color="#c9d0de"/>
        </linearGradient>
        <linearGradient id="swooshGreen" x1="0" y1="0" x2="1" y2="1">
          <stop offset="0" stop-color="#c5e07a"/>
          <stop offset="1" stop-color="#8cc63f"/>
        </linearGradient>
      </defs>
      <rect class="center-field" width="1180" height="272" fill="url(#centerGlow)"/>
      <path class="crowd-area" role="img" aria-label="Silhouettes of business people walking in front of a faint world map"
            d="M0 0 H430 C360 40 380 200 215 272 H0 Z" fill="url(#crowdTone)"/>
      <path class="left-swoosh" d="M430 0 H458 C388 60 405 225 232 272 H215 C380 200 360 40 430 0 Z" fill="url(#swooshGreen)"/>
      <path class="right-panel" d="M690 0 H1180 V272 H920 C820 250 820 40 690 0 Z" fill="var(--panel-green)"/>
      <path class="right-band" d="M676 0 H700 C838 40 838 248 938 272 H905 C806 255 812 40 676 0 Z" fill="var(--band-dark)"/>
    </svg>

    <div class="brand">
      <span class="brand-square"></span>
      <span class="brand-name">Dovrin</span>
    </div>
    <div class="brand-sub">Dovrin Marketing Communication Ltd.</div>

    <h1 class="headline">
      <span class="years">16 YEARS</span>
      <span class="success">OF SUCCES</span>
    </h1>

    <p class="services">Working with global tech<br>companies in Israel, PR &amp;<br>Social Media, strategic<br>and crisis management</p>

    <div class="cta">SEE MORE DETAILS</div>
  </section>
</div>
</body>
</html>
```